Scent Marketing Solutions by Vapolinth

We need to create 12 page brochure (including the cover and back page) for our Scent Marketing line of products.

The brochure size is 18 cm x 18 cm.

Our competitors are www.breeze-olfa.example and www.nosquell.example
Updates

Hi Designers, 

The budget for this project has been increased to $300. This is a 12 page brochure of size 18cm x 18cm.

Thank you.

Hi all designers,

I uploaded a new brochure draft with the write up in pdf.
I understand that some of you could not open the original file in powerpoint.

Thank you.

Hi Designers,

I added the brochure write up in Word and PDF format. I understand some of you have troubles with it in the earlier files uploaded.

Thank you.

Target Market(s)

B2B audience, such as visual merchandisers of retail brands, hotel managers, real estate property managers etc.

Industry/Entity Type

Marketing

Requirements
Must have
• Our corporate identity uses a lot of white, hence this must be reflected in the brochure.
Our products are high-tech and environmentally friendly, so this must again be reflected in the design.
We want to make the brochure attractive and easy to read, hence would like to allocate more space for photos and pictures and keep the brochure as spacious as possible.
Nice to have
• Since the product is related to the air (it scents the air), we would like to have a design feature that reflects this and is repeated throughout the brochure. It can be a pattern or logo.
Should not have
• Avoid using a lot of bright colors

```html
<!DOCTYPE html>
<html lang="en">
<head>
<meta charset="utf-8">
<title>Vapolinth – Unleash the Power of Scent Marketing</title>
<link rel="stylesheet" href="https://fonts.googleapis.com/css2?family=Josefin+Sans:wght@300&family=Hind:wght@400;600&display=swap">
<style>
  :root {
    --page-white: #ffffff;
    --title-grey: #8a8a8c;
    --body-ink: #1c1c1c;
    --mist-blue: #dfe6f0;
    --mist-pale: #f1f4f9;
    --photo-deep: #2e3a2a;
    --photo-mid: #5d6b4c;
    --photo-skin: #b89480;
    --photo-light: #dfe3ea;
  }
  html, body {
    margin: 0;
    padding: 0;
    width: 1200px;
    height: 600px;
    overflow: hidden;
    background: var(--page-white);
  }
  .spread {
    position: relative;
    width: 1200px;
    height: 600px;
    background: var(--page-white);
    overflow: hidden;
  }
  .hero-photo {
    position: absolute;
    left: 50px;
    top: 50px;
    width: 500px;
    height: 500px;
    background:
      radial-gradient(ellipse 38% 45% at 58% 52%, var(--photo-skin) 0%, rgba(184,148,128,0.5) 45%, rgba(184,148,128,0) 75%),
      radial-gradient(ellipse 30% 30% at 85% 20%, var(--photo-light) 0%, rgba(223,227,234,0) 70%),
      radial-gradient(ellipse 35% 30% at 15% 85%, #9aa6c2 0%, rgba(154,166,194,0) 70%),
      linear-gradient(135deg, var(--photo-mid) 0%, var(--photo-deep) 55%, #1f241c 100%);
  }
  .air-mist {
    position: absolute;
    left: 550px;
    top: 340px;
    width: 650px;
    height: 260px;
    background:
      radial-gradient(ellipse 70% 45% at 60% 45%, var(--mist-blue) 0%, rgba(223,230,240,0) 100%),
      linear-gradient(180deg, rgba(255,255,255,0) 0%, var(--mist-pale) 45%, rgba(255,255,255,0) 100%);
  }
  .copy {
    position: absolute;
    left: 600px;
    top: 46px;
    width: 576px;
    text-align: center;
    font-family: "Hind", "Segoe UI", sans-serif;
    color: var(--body-ink);
  }
  .copy__title {
    margin: 0 0 24px;
    font-family: "Josefin Sans", "Gill Sans", sans-serif;
    font-weight: 300;
    font-size: 31px;
    line-height: 39px;
    letter-spacing: 1px;
    color: var(--title-grey);
  }
  .copy__intro {
    margin: 0 0 8px;
    font-size: 11.5px;
    line-height: 17px;
  }
  .copy__lead {
    margin: 0 0 4px;
    font-size: 11.5px;
    line-height: 17px;
    font-weight: 600;
  }
  .benefits {
    list-style: none;
    margin: 0 0 4px;
    padding: 0;
    font-size: 11.5px;
    font-weight: 600;
  }
  .benefits li {
    line-height: 23px;
  }
  .benefits li::before {
    content: "\2605\00a0";
    color: #555;
  }
  .copy__closing {
    margin: 0;
    font-size: 11.5px;
    line-height: 18px;
  }
</style>
</head>
<body>
  <main class="spread">
    <div class="hero-photo" role="img" aria-label="Photograph of a woman gazing thoughtfully through a café window, holding a white cup"></div>

    <div class="air-mist" role="img" aria-label="Soft airy wave decoration in pale blue and white"></div>

    <section class="copy">
      <h1 class="copy__title">UNLEASH THE POWER OF<br>SCENT MARKETING</h1>
      <p class="copy__intro">All day long, consumers’ eyes and ears are bombarded by traditional advertising and marketing messages.<br>This causes sensory overload, and more importantly, it causes consumers to tune your company out.</p>
      <p class="copy__lead">With scent marketing solutions from Vapolinth, you can use a specific scent to:</p>
      <ul class="benefits">
        <li>Get the attention of your customers</li>
        <li>Differentiate your brand</li>
        <li>Increase the effectiveness of your marketing communications</li>
        <li>Influence your customers’ feelings and responses</li>
      </ul>
      <p class="copy__closing">When combined with other sensory triggers, you can create a long-lasting sensory and emotional<br>connection with your customers</p>
    </section>
  </main>
</body>
</html>
```